The Timber Loft

We need a business card design for our wardrobe company.
Please visit our website www.zorvelcabinets.com to get an idea of who we are.

```html
<!DOCTYPE html>
<html lang="en">
<head>
<meta charset="utf-8">
<title>The Timber Loft — Business Card</title>
<link rel="stylesheet" href="https://fonts.googleapis.com/css2?family=Open+Sans:wght@400;600;700&display=swap">
<style>
  :root {
    --page-bg: #1b1b1c;
    --card-frost: #8d8f91;
    --card-frost-light: #a3a5a7;
    --card-edge: rgba(255, 255, 255, 0.35);
    --ink: #f4f5f6;
    --ink-soft: rgba(255, 255, 255, 0.85);
  }
  * { box-sizing: border-box; margin: 0; padding: 0; }
  html, body {
    width: 1200px;
    height: 1000px;
    overflow: hidden;
  }
  body {
    background: var(--page-bg);
    font-family: "Open Sans", Arial, sans-serif;
    display: flex;
    align-items: center;
    justify-content: center;
  }
  .business-card {
    position: relative;
    width: 880px;
    height: 520px;
    border-radius: 26px;
    background: linear-gradient(135deg, var(--card-frost-light) 0%, var(--card-frost) 100%);
    border: 2px solid var(--card-edge);
    color: var(--ink);
    display: flex;
    align-items: center;
    padding: 0 64px;
    gap: 56px;
  }
  .brand-block {
    width: 320px;
    flex: none;
    display: flex;
    flex-direction: column;
    gap: 10px;
  }
  .brand-name {
    display: flex;
    align-items: center;
    gap: 12px;
    font-size: 26px;
    font-weight: 600;
    letter-spacing: 0.02em;
    text-transform: uppercase;
    line-height: 1.1;
    white-space: nowrap;
  }
  .brand-square {
    flex: none;
    width: 22px;
    height: 22px;
    background: var(--ink);
  }
  .brand-tagline {
    font-size: 21px;
    font-weight: 600;
    color: var(--ink-soft);
    white-space: nowrap;
  }
  .contact-block {
    display: flex;
    flex-direction: column;
  }
  .person-name {
    font-size: 44px;
    font-weight: 700;
    line-height: 1;
  }
  .person-role {
    font-size: 15px;
    letter-spacing: 0.3em;
    text-transform: uppercase;
    color: var(--ink-soft);
    margin: 6px 0 22px;
  }
  .contact-list { list-style: none; display: flex; flex-direction: column; gap: 8px; }
  .contact-item {
    display: flex;
    align-items: flex-start;
    gap: 12px;
    font-size: 21px;
    line-height: 1.3;
    white-space: nowrap;
  }
  .contact-icon { flex: none; width: 20px; height: 20px; margin-top: 4px; fill: var(--ink); }
</style>
</head>
<body>
  <article class="business-card">
    <section class="brand-block">
      <div class="brand-name"><span class="brand-square"></span>The Timber Loft</div>
      <p class="brand-tagline">Built Square, Built to Last</p>
    </section>
    <section class="contact-block">
      <h1 class="person-name">John Doe</h1>
      <p class="person-role">Director</p>
      <ul class="contact-list">
        <li class="contact-item">
          <svg class="contact-icon" viewBox="0 0 24 24" aria-hidden="true"><path d="M6.6 10.8a15 15 0 0 0 6.6 6.6l2.2-2.2a1 1 0 0 1 1-.25 11.4 11.4 0 0 0 3.6.6 1 1 0 0 1 1 1V20a1 1 0 0 1-1 1A17 17 0 0 1 3 4a1 1 0 0 1 1-1h3.5a1 1 0 0 1 1 1c0 1.25.2 2.45.6 3.6a1 1 0 0 1-.25 1z"/></svg>
          0207 555 0184
        </li>
        <li class="contact-item">
          <svg class="contact-icon" viewBox="0 0 24 24" aria-hidden="true"><path d="M2 6a2 2 0 0 1 2-2h16a2 2 0 0 1 2 2v.4l-10 6-10-6zm0 2.7 10 6 10-6V18a2 2 0 0 1-2 2H4a2 2 0 0 1-2-2z"/></svg>
          info@zorvelcabinets.com
        </li>
        <li class="contact-item">
          <svg class="contact-icon" viewBox="0 0 24 24" aria-hidden="true"><path d="M12 2a7 7 0 0 0-7 7c0 5 7 13 7 13s7-8 7-13a7 7 0 0 0-7-7zm0 9.5A2.5 2.5 0 1 1 12 6.5a2.5 2.5 0 0 1 0 5z"/></svg>
          <span>Alder Court, 42 Mill Lane,<br>London N4 7QP</span>
        </li>
      </ul>
    </section>
  </article>
</body>
</html>
```